Martin K Doyle DDS (dentist) needs a business card/business logo design

I would like an eye-catchingly conservative or elegant graphic presentation of my business name with the elements: prevention, restoration, and cosmetics (these are the services I'd like to emphasize) .
The business card would have room for address lines, phone and fax, web address. No standard teeth or oral representations please. Should communicate professionalism. Whatever color scheme works.

Thank you

Target Market(s)

I just want a good looking business card

Industry/Entity Type

Conservative

Contact Information for Business Card

Adress: 4173 Brisford Ave Lakewood CA 90716 Phone: 562 430 5926 FAX 562 430 6384 Web: Pinegrovedental.com

Font styles to use
Sans Serif

Colors
0255a3

Requirements
Must have
• business name with the elements: prevention, restoration, and cosmetics (these are the services I'd like to emphasize)
• communicates professionalism
Nice to have
• eye catching but not flashy graphics
Should not have
• no pictures of teeth or dental instruments

```html
<!DOCTYPE html>
<html lang="en">
<head>
<meta charset="utf-8">
<title>Martin K Doyle DDS – Business Card</title>
<link rel="stylesheet" href="https://fonts.googleapis.com/css2?family=Ubuntu:wght@400;500;700&display=swap">
<style>
  :root {
    --page-bg: #e9eaec;
    --card-grey: #8f949c;
    --card-teal: #017a88;
    --brand-red: #b20d0d;
    --tab-white: #ffffff;
    --tab-text: #8b8e93;
    --contact-text: #ffffff;
  }
  html, body {
    margin: 0;
    width: 1200px;
    height: 1000px;
    overflow: hidden;
    background: var(--page-bg);
    font-family: "Ubuntu", sans-serif;
  }
  .card {
    position: absolute;
    left: 120px;
    top: 230px;
    width: 960px;
    height: 540px;
    background: var(--card-grey);
    box-shadow: 0 10px 30px rgba(0,0,0,0.18);
    overflow: hidden;
  }
  .card__band {
    position: absolute;
    left: 0;
    top: 210px;
    width: 100%;
    height: 270px;
    background: var(--card-teal);
  }
  .brand {
    position: absolute;
    left: 52px;
    top: 58px;
    display: flex;
    align-items: center;
    gap: 16px;
  }
  .brand__mark {
    width: 44px;
    height: 44px;
    background: var(--brand-red);
  }
  .brand__name {
    font-size: 44px;
    font-weight: 500;
    color: var(--brand-red);
    letter-spacing: 0.5px;
  }
  .services {
    position: absolute;
    left: 52px;
    top: 160px;
    margin: 0;
    font-size: 25px;
    font-weight: 700;
    color: var(--brand-red);
  }
  .name-tab {
    position: absolute;
    left: 560px;
    top: 158px;
    width: 400px;
    height: 104px;
    background: var(--tab-white);
    border-radius: 34px 0 0 34px;
    box-sizing: border-box;
    padding: 22px 40px 0 0;
    text-align: right;
    color: var(--tab-text);
  }
  .name-tab__name {
    margin: 0;
    font-size: 32px;
    font-weight: 700;
    line-height: 1.1;
  }
  .name-tab__practice {
    margin: 4px 0 0;
    font-size: 24px;
    font-weight: 400;
  }
  .contact {
    position: absolute;
    left: 52px;
    top: 262px;
    margin: 0;
    padding: 0;
    list-style: none;
    color: var(--contact-text);
    font-size: 26px;
    font-weight: 500;
    line-height: 46px;
  }
</style>
</head>
<body>
  <div class="card">
    <div class="card__band"></div>

    <div class="brand">
      <div class="brand__mark"></div>
      <div class="brand__name">Martin K Doyle DDS</div>
    </div>

    <p class="services">Prevention, Restoration and Cosmetics</p>

    <div class="name-tab">
      <p class="name-tab__name">Martin K Doyle DDS</p>
      <p class="name-tab__practice">Pinegrove Dental Care</p>
    </div>

    <ul class="contact">
      <li>Phone: 562- 430- 5926</li>
      <li>Fax: 562- 430- 6384</li>
      <li>Website: www.Pinegrovedental.com</li>
      <li>Address: 4173 Brisford Ave, Lakewood, CA 90716</li>
    </ul>
  </div>
</body>
</html>
```